Plivora Design Project

I need new cover graphics for my father's plivora page. He is running for major of our town in Puerto Rico.
Need his name on the cover: Mateo Brunal
And the position, town and year: Alcalde Carolina 2012
As a default background color you can use the blue in the current cover graphic, or go here for color ideas http://www.lumbrevecinal2012.com/indexContinuar.php
I really would like to see something that incorporates some of the pictures I have uploaded of him with people in the town, or with popular leaders. He is the guy with gray hair.
Below is the target plivora page. Thanks
https://www.plivora.com/mateobrunal.quesada

```html
<!DOCTYPE html>
<html lang="es">
<head>
<meta charset="utf-8">
<title>Mateo Brunal · Alcalde Carolina 2012</title>
<link href="https://fonts.googleapis.com/css2?family=Open+Sans:wght@400;600;700&family=Ubuntu:wght@500;700&display=swap" rel="stylesheet">
<style>
:root{
  --bar:#3b5998;
  --bar-dark:#29447e;
  --page:#e9eaed;
  --panel:#ffffff;
  --soft:#f2f2f2;
  --line:#d3d6db;
  --link:#3b5998;
  --ink:#141823;
  --muted:#6a7180;
  --cover-deep:#1c2472;
  --cover-mid:#2e3a9e;
  --cover-light:#5566c8;
  --frame:#fbfbf8;
}
*{margin:0;padding:0;box-sizing:border-box}
html,body{width:1200px;height:914px;overflow:hidden}
body{position:relative;background:var(--page);font-family:"Open Sans",Arial,sans-serif;color:var(--ink);font-size:13px}
.topbar{position:absolute;left:0;top:0;width:1200px;height:46px;background:var(--bar);border-bottom:1px solid var(--bar-dark)}
.brand{position:absolute;left:144px;top:7px;color:#fff;font-weight:700;font-size:26px;letter-spacing:-.5px}
.nav-icons{position:absolute;left:268px;top:15px;display:flex;gap:10px}
.nav-icons span{width:17px;height:17px;border-radius:50%;background:#1f3566}
.search{position:absolute;left:366px;top:12px;width:425px;height:27px;background:#fff;border:1px solid var(--bar-dark);font-size:13px;color:#777;padding:4px 6px}
.search svg{position:absolute;right:6px;top:5px}
.column{position:absolute;left:145px;top:46px;width:1045px;height:868px;background:var(--panel)}
.cover{position:absolute;left:0;top:0;width:1038px;height:387px;overflow:hidden;
  background:radial-gradient(ellipse 520px 330px at 560px 150px,var(--cover-light),transparent 70%),
  linear-gradient(100deg,var(--cover-deep) 0%,var(--cover-mid) 45%,var(--cover-deep) 100%)}
.cover-title{position:absolute;left:18px;top:92px;width:275px;text-align:center;color:#fff;font-family:"Ubuntu",sans-serif}
.cover-title .name{font-size:43px;font-weight:700;line-height:1.1}
.cover-title .role{font-size:25px;font-weight:700;margin-top:8px}
.snap{position:absolute;background:var(--frame);padding:10px;box-shadow:0 3px 10px rgba(0,0,0,.45)}
.snap div{width:100%;height:100%}
.snap-one{left:319px;top:27px;width:250px;height:336px;transform:rotate(-2deg)}
.snap-one div{background:linear-gradient(160deg,#efe6c9,#3a8f8a 55%,#e9e9ef)}
.snap-two{left:572px;top:72px;width:254px;height:311px;transform:rotate(3deg)}
.snap-two div{background:linear-gradient(170deg,#4f8a3c,#b49680 45%,#6e8ec4)}
.snap-three{left:801px;top:13px;width:238px;height:314px;transform:rotate(3deg)}
.snap-three div{background:linear-gradient(170deg,#6b5a45,#c9a48c 40%,#8fa7c8)}
.avatar{position:absolute;left:27px;top:239px;width:208px;height:206px;background:#fff;padding:5px;border:1px solid var(--line);box-shadow:0 1px 3px rgba(0,0,0,.3);z-index:2}
.avatar div{width:100%;height:100%;background:linear-gradient(160deg,#e6ddc0,#c7c4c9 45%,#2f8c84)}
.profile-name{position:absolute;left:252px;top:404px;width:330px;font-size:24px;font-weight:700;line-height:1.25;color:#1d2a49}
.actions{position:absolute;left:615px;top:405px;display:flex;gap:13px}
.btn-group{display:flex}
.btn{height:30px;padding:0 10px;border:1px solid #a9acb4;background:linear-gradient(#fafafa,#e8e9ec);font-weight:600;font-size:15px;color:#333;display:flex;align-items:center;gap:5px;white-space:nowrap}
.btn-group .btn+.btn{border-left:none}
.btn.gear{width:51px;justify-content:center}
.facts{position:absolute;left:0;top:480px;width:400px;height:90px;background:var(--soft);border-top:1px solid var(--line);padding:6px 0 0 30px;font-size:13px;line-height:20px}
.facts li{list-style:none;display:block}
.facts i{width:8px;height:8px;background:#8d939e;border-radius:2px;display:inline-block;margin-right:8px;vertical-align:middle}
.facts a,.link{color:var(--link);text-decoration:none}
.about-link{position:absolute;left:54px;top:582px;font-size:13px}
.tiles{position:absolute;left:410px;top:481px;display:flex;gap:10px}
.tile{width:136px}
.tile .art{height:90px;border:1px solid var(--line)}
.tile p{margin-top:8px;font-size:13px;color:var(--link)}
.tile p span{color:var(--muted)}
.art-photos{background:linear-gradient(#fafafa,#e4e4e4)}
.art-map{background:linear-gradient(160deg,#c4d3e8,#dfe7f2)}
.art-likes{background:linear-gradient(90deg,#1b2a6b 45%,#e9cdb3 50%,#c79a73)}
.art-subs{background:#d7dde9;display:flex;align-items:center;justify-content:center;font-size:34px;font-weight:700;color:#1d2a49}
.prompt{position:absolute;left:14px;top:631px;width:1010px;height:43px;background:#eceff5;border-top:1px solid var(--line);padding:12px 10px;font-size:12.5px;color:var(--muted);white-space:nowrap}
.prompt b{color:var(--ink);font-size:15px;margin-right:8px}
.info{position:absolute;left:16px;top:694px;width:485px}
.section-head{font-weight:700;font-size:14px;padding-bottom:8px;border-bottom:1px solid var(--line)}
.about-row{display:flex;margin-top:12px}
.about-row .label{width:82px;color:var(--muted);font-weight:700}
.about-row .text{flex:1;font-size:13px;line-height:18.3px}
.divider{position:absolute;left:520px;top:694px;width:1px;height:174px;background:var(--line)}
.albums{position:absolute;left:538px;top:694px;width:486px}
.album-row{display:flex;gap:6px;margin-top:14px}
.album{width:120px;height:117px;position:relative}
.album span{position:absolute;left:0;bottom:0;width:100%;padding:4px 6px;font-size:12.5px;color:#fff;background:linear-gradient(transparent,rgba(0,0,0,.65))}
.al-timeline{background:linear-gradient(#f7f7f7,#d9d9d9)}
.al-cover{background:linear-gradient(160deg,#10218a,#2d3fb6 60%,#0d1a66)}
.al-mobile{background:#d9dbe0}
.al-profile{background:linear-gradient(#2a4fb0 12%,#dad6d3 13%,#6f8bd8)}
</style>
</head>
<body>
<header class="topbar">
  <div class="brand">plivora</div>
  <div class="nav-icons"><span></span><span></span><span></span></div>
  <div class="search">Search for people, places and things
    <svg width="14" height="14" viewBox="0 0 14 14"><circle cx="5.5" cy="5.5" r="4" fill="none" stroke="#777" stroke-width="1.6"/><line x1="8.5" y1="8.5" x2="13" y2="13" stroke="#777" stroke-width="1.8"/></svg>
  </div>
</header>

<main class="column">
  <section class="cover">
    <div class="cover-title">
      <div class="name">Mateo Brunal</div>
      <div class="role">Alcalde Carolina 2012</div>
    </div>
    <figure class="snap snap-one"><div role="img" aria-label="Candidate with gray hair smiling and giving a thumbs up beside a supporter"></div></figure>
    <figure class="snap snap-two"><div role="img" aria-label="Candidate in sunglasses with two town residents outdoors"></div></figure>
    <figure class="snap snap-three"><div role="img" aria-label="Candidate standing beside an older community leader"></div></figure>
  </section>

  <div class="avatar"><div role="img" aria-label="Profile photo of the candidate with a supporter"></div></div>
  <h1 class="profile-name">Mateo Brunal Alcalde de Carolina</h1>

  <div class="actions">
    <div class="btn-group">
      <span class="btn">+ Add Friend</span>
      <span class="btn"><svg width="10" height="10" viewBox="0 0 10 10"><circle cx="1.5" cy="8.5" r="1.4" fill="#555"/><path d="M0 4.5a5.5 5.5 0 0 1 5.5 5.5M0 1a9 9 0 0 1 9 9" fill="none" stroke="#555" stroke-width="1.6"/></svg>Subscribe</span>
    </div>
    <div class="btn-group">
      <span class="btn">Message</span>
      <span class="btn gear">⚙ ▾</span>
    </div>
  </div>

  <ul class="facts">
    <li><i></i>Lives in <a href="#">Carolina</a>, <a href="#">Puerto Rico</a></li>
    <li><i></i>Married</li>
    <li><i></i>Knows Español, Inglés</li>
    <li><i></i>Male</li>
  </ul>
  <a class="about-link link" href="#">About</a>

  <div class="tiles">
    <div class="tile"><div class="art art-photos" role="img" aria-label="Latest timeline photo of a ballot"></div><p>Photos</p></div>
    <div class="tile"><div class="art art-map" role="img" aria-label="World map of visited places"></div><p>Map</p></div>
    <div class="tile"><div class="art art-likes" role="img" aria-label="Pages liked by the candidate"></div><p>Likes <span>26</span></p></div>
    <div class="tile"><div class="art art-subs">12</div><p>Subscribers</p></div>
  </div>

  <div class="prompt"><b>Do you know Mateo Brunal?</b>If you know Mateo Brunal, <a class="link" href="#">send him a friend request</a> or <a class="link" href="#">message him</a>. You can also <a class="link" href="#">subscribe</a> to his public posts.</div>

  <section class="info">
    <div class="section-head">Info</div>
    <div class="about-row">
      <div class="label">About</div>
      <div class="text">CAROLINA SE VESTIRÁ DE AZUL EN EL 2012<br>Carolina, Puerto Rico (23 de octubre de 2011)- En una tarde brillante y llena de entusiasmo y junto a cientos de amigos, simpatizantes y por supuesto miembros de la plana mayor del PVN, el Sr. Mateo Brunal Quesada, anunció su interés a aspirar a la poltrona municipal de Carolina.<br><br>"A partir de hoy cambia la historia de Carolina y esta Tierra de</div>
    </div>
  </section>

  <div class="divider"></div>

  <section class="albums">
    <div class="section-head">▣ Albums</div>
    <div class="album-row">
      <div class="album al-timeline" role="img" aria-label="Timeline photos album with a ballot"><span>Timeline Photos</span></div>
      <div class="album al-cover" role="img" aria-label="Cover photos album with a blue campaign poster"><span>Cover Photos</span></div>
      <div class="album al-mobile" role="img" aria-label="Mobile uploads album"><span>Mobile Uploads</span></div>
      <div class="album al-profile" role="img" aria-label="Profile pictures album with the candidate"><span>Profile Pictures</span></div>
    </div>
  </section>
</main>
</body>
</html>
```